Industrial Professional Business Card Design (Vantrel Systems)

Would like professional looking business cards. Not too busy leaning towards minimal. Should have a slogan like:
"Industrial Automation and Control".

We are a tech company that programs industrial PLC computers. We also develop custom hardware solutions. Please use the logo for inspiration.

Target Market(s)

Mining, industrial, processing, automation, factory

Industry/Entity Type

Engineering

Contact Information for Business Card

Name, phone, email, website. job title.

Font styles to use
Other font styles liked:
• droid sans

Requirements
Must have
• Use colours that go well with the logo. Not too busy design.

```html
<!DOCTYPE html>
<html lang="en">
<head>
<meta charset="utf-8">
<title>Vantrel Systems — Business Card</title>
<link rel="stylesheet" href="https://fonts.googleapis.com/css2?family=Noto+Sans:wght@400;700&display=swap">
<style>
  :root {
    --bg: #3b3c3e;
    --navy: #182656;
    --teal: #22729c;
    --orange: #f06a22;
    --white: #ffffff;
    --card-w: 600px;
    --card-h: 343px;
  }
  * { margin: 0; padding: 0; box-sizing: border-box; }
  html, body {
    width: 1200px; height: 901px; overflow: hidden;
    background: var(--bg);
    font-family: "Noto Sans", "Droid Sans", sans-serif;
  }
  .card {
    position: absolute;
    width: var(--card-w); height: var(--card-h);
    left: 300px;
    overflow: hidden;
    background: linear-gradient(30deg, var(--navy) 0%, #1d4477 50%, var(--teal) 100%);
    box-shadow: 0 8px 22px rgba(0,0,0,.45);
    color: var(--white);
  }
  .card--front { top: 76px; }
  .card--back  { top: 478px; }

  .brand {
    position: absolute; inset: 0;
    display: flex; flex-direction: column; align-items: center; justify-content: center;
  }
  .brand__row { display: flex; align-items: center; gap: 14px; }
  .brand__dot {
    width: 34px; height: 34px; border-radius: 50%;
    background: var(--white);
  }
  .brand__name {
    font-size: 40px; font-weight: 400; letter-spacing: .5px;
    color: var(--white); line-height: 1.2;
  }
  .brand__slogan {
    margin-top: 10px;
    font-size: 13px; font-weight: 400; letter-spacing: 2px;
    text-transform: uppercase; color: var(--white); opacity: .85;
  }

  .back-art { position: absolute; inset: 0; }
  .back-brand {
    position: absolute; left: 372px; top: 150px; width: 210px;
    text-align: center;
    font-size: 24px; font-weight: 700; color: var(--navy); line-height: 1.2;
  }

  .contact {
    position: absolute; left: 40px; top: 92px; width: 250px;
  }
  .contact__name { font-size: 22px; font-weight: 700; line-height: 1.1; }
  .contact__title { font-size: 16px; margin-top: 2px; opacity: .95; }
  .contact__address { font-size: 14px; line-height: 1.3; margin-top: 26px; }
  .contact__list { list-style: none; margin-top: 26px; font-size: 14px; line-height: 1.55; }
  .contact__list li { display: flex; align-items: center; gap: 10px; white-space: nowrap; }
  .contact__list svg { width: 13px; height: 13px; flex: none; }
</style>
</head>
<body>

<section class="card card--front" aria-label="Card front">
  <div class="brand">
    <div class="brand__row">
      <span class="brand__dot"></span>
      <span class="brand__name">Vantrel Systems</span>
    </div>
    <p class="brand__slogan">Industrial Automation and Control</p>
  </div>
</section>

<section class="card card--back" aria-label="Card back">
  <svg class="back-art" viewBox="0 0 600 343" width="600" height="343" aria-hidden="true">
    <ellipse cx="498" cy="150" rx="218" ry="196" fill="none" stroke="var(--orange)" stroke-width="5"/>
    <ellipse cx="505" cy="143" rx="218" ry="196" fill="var(--white)"/>
  </svg>
  <div class="back-brand">Vantrel Systems</div>

  <div class="contact">
    <p class="contact__name">Marcus Ellery</p>
    <p class="contact__title">Manager</p>
    <p class="contact__address">48 Foundry Lane, Halden<br>Ohio, OH 44618</p>
    <ul class="contact__list">
      <li>
        <svg viewBox="0 0 16 16"><path fill="#fff" d="M3.6 1.2l2.3 2.6-1.3 1.8c.9 2 2.7 3.8 4.7 4.7l1.8-1.3 2.6 2.3-1.4 2.2C7.2 13.3 2.7 8.8 1.4 3.7z"/></svg>
        555-018-2140
      </li>
      <li>
        <svg viewBox="0 0 16 16"><rect x="1.5" y="3.5" width="13" height="9" fill="none" stroke="#fff" stroke-width="1.5"/><path d="M1.5 3.5l6.5 5 6.5-5" fill="none" stroke="#fff" stroke-width="1.5"/></svg>
        m.ellery@vantrelmail.com
      </li>
      <li>
        <svg viewBox="0 0 16 16"><circle cx="8" cy="8" r="6.5" fill="none" stroke="#fff" stroke-width="1.4"/><ellipse cx="8" cy="8" rx="2.8" ry="6.5" fill="none" stroke="#fff" stroke-width="1.2"/><path d="M1.5 8h13" stroke="#fff" stroke-width="1.2"/></svg>
        www.vantrelsystems.com
      </li>
    </ul>
  </div>
</section>

</body>
</html>
```